Solvane Vitality MediSpa Brochure

We need a new brochure design. The old is attached.

We are wanting a three panel brochure for med spa designed and ready for print. The brochure will have content and images on both sides. We attached the old brochure in pdf format. The content needs to stay as on the attached pdf but please feel free to offer new designs. The color needs to match the attached logo, which is a light blue and teal. All images we want on the brochure are also attached.

The design must have an 1/8 in space from each edge for printing purposes

Target Market(s)

Men and Women

Industry/Entity Type

Wellness

Font styles to use
Sans Serif

Colors
34a6d7
33b8a4

Requirements
Must have
• soft curves. must have a 1/8 in space on all edges (including interior) to give bleed space for printing. Use content written on attached brochure.

```html
<!DOCTYPE html>
<html lang="en">
<head>
<meta charset="utf-8">
<title>Solvane Vitality MediSpa – Tri-fold Brochure</title>
<link href="https://fonts.googleapis.com/css2?family=Oswald:wght@500&family=PT+Sans:ital,wght@0,400;0,700;1,400&display=swap" rel="stylesheet">
<style>
  :root{
    --teal:#17a6aa;
    --teal-deep:#12949a;
    --cyan:#22d3dc;
    --charcoal:#4a4b4e;
    --ink:#333436;
    --paper:#ffffff;
    --backdrop:#7e7e81;
    --head:'Oswald', sans-serif;
    --body:'PT Sans', sans-serif;
  }
  *{margin:0;padding:0;box-sizing:border-box}
  html,body{width:1200px;height:1200px;overflow:hidden;background:var(--backdrop)}
  .canvas{position:relative;width:1200px;height:1200px}
  .brochure{
    position:absolute;left:39px;top:201px;width:860px;height:612px;
    transform:scale(1.305);transform-origin:0 0;
    background:var(--paper);overflow:hidden;font-family:var(--body);
    box-shadow:0 2px 10px rgba(0,0,0,.25);
  }
  .shapes,.photo{position:absolute;left:0;top:0}
  .txt{position:absolute}
  .section-title{font-family:var(--head);font-weight:500;font-size:11px;color:var(--paper);margin-bottom:4px}
  .section-copy{font-size:8.6px;line-height:12px;color:var(--paper)}
  .intro{left:18px;top:20px;width:258px}
  .why{left:18px;top:102px;width:238px}
  .members{left:18px;top:214px;width:180px}
  .member-list{list-style:none;margin-top:10px;font-size:9.6px;line-height:13px;color:var(--paper)}
  .member-list li{margin-bottom:7px}
  .member-list li::before{content:"• ";font-size:7px}
  .learn{left:18px;top:505px}
  .learn-title{font-size:14px;color:var(--teal);margin-bottom:7px}
  .learn-url{font-size:10.5px;color:var(--ink);letter-spacing:-.2px}
  .contact{left:323px;top:27px;width:240px;color:var(--paper)}
  .contact-title{font-size:12.5px;color:var(--cyan);margin-bottom:2px;font-weight:400}
  .contact-line{font-size:9px;line-height:13px;display:flex;align-items:center;gap:4px}
  .contact-line svg{flex:none}
  .contact-indent{padding-left:10px}
  .contact-gap{height:7px}
  .doctor{left:347px;top:403px;width:200px}
  .doctor-name{font-family:var(--head);font-weight:500;font-size:10.5px;color:var(--ink);margin-bottom:10px}
  .doctor-name span{color:var(--teal)}
  .quote{font-style:italic;font-size:8.4px;line-height:12px;color:var(--ink);margin-bottom:7px}
  .brand{left:600px;top:30px;width:240px;text-align:center}
  .brand-name{display:flex;align-items:center;justify-content:center;gap:6px;font-size:17px;color:var(--teal);letter-spacing:.4px}
  .brand-dot{width:11px;height:11px;border-radius:50%;background:var(--teal);flex:none}
  .tagline{margin-top:20px;font-family:var(--head);font-weight:500;font-size:16.5px;color:var(--charcoal)}
  .audience{left:612px;top:447px;font-family:var(--head);font-weight:500;font-size:23px;color:var(--paper)}
  .services{left:614px;top:486px;display:grid;grid-template-columns:104px 110px;font-size:9px;line-height:13.5px;color:var(--paper);list-style:none}
  .services li::before{content:"• "}
  .callout{
    left:614px;top:545px;width:211px;height:49px;border-radius:25px;
    background:var(--paper);border:2px solid #8d8e91;text-align:center;
    color:var(--ink);padding-top:5px;box-shadow:0 1px 3px rgba(0,0,0,.3);
  }
  .callout-phone{font-size:13px;font-weight:700}
  .callout-url{font-size:10.5px;letter-spacing:-.2px}
</style>
</head>
<body>
<main class="canvas">
  <article class="brochure">

    <svg class="shapes" width="860" height="612" viewBox="0 0 860 612" aria-hidden="true">
      <!-- left panel teal field -->
      <path fill="var(--teal)" d="M0,0 H298 C290,80 275,140 262,195 C240,260 205,300 200,350 C198,400 225,440 270,470 L0,470 Z"/>
      <!-- middle panel charcoal field -->
      <path fill="var(--charcoal)" d="M296,0 H520 C520,60 540,110 576,125 L576,150 C510,170 480,230 470,290 C462,350 400,380 340,400 C320,420 310,460 305,520 L296,520 Z"/>
      <!-- ribbons following the left curve -->
      <path fill="none" stroke="var(--cyan)" stroke-width="7" transform="translate(10,0)" d="M298,0 C290,80 275,140 262,195 C240,260 205,300 200,350 C198,400 225,440 270,470 C290,500 305,560 320,612"/>
      <path fill="none" stroke="var(--teal)" stroke-width="6" transform="translate(20,0)" d="M298,0 C290,80 275,140 262,195 C240,260 205,300 200,350 C198,400 225,440 270,470 C290,500 305,560 320,612"/>
      <!-- lower left bands -->
      <path fill="var(--cyan)" d="M0,428 C130,416 250,445 320,530 L345,612 H330 L300,540 C230,470 120,438 0,448 Z"/>
      <path fill="var(--charcoal)" d="M0,448 C120,438 230,470 300,540 L330,612 H300 C250,530 150,490 0,495 Z"/>
      <!-- middle panel top ribbons -->
      <path fill="none" stroke="var(--teal)" stroke-width="7" d="M532,0 C532,58 552,100 584,112"/>
      <path fill="none" stroke="var(--cyan)" stroke-width="5" d="M505,232 C530,195 552,168 584,150"/>
      <!-- panel fold shading -->
      <rect x="286" y="0" width="10" height="612" fill="rgba(0,0,0,.05)"/>
      <rect x="571" y="0" width="10" height="612" fill="rgba(0,0,0,.05)"/>
      <!-- cover: side curve and teal base -->
      <path fill="none" stroke="var(--charcoal)" stroke-width="10" d="M566,150 C585,250 585,400 572,612"/>
      <path fill="var(--teal)" d="M580,395 C640,425 760,420 860,405 V612 H580 Z"/>
      <path fill="none" stroke="var(--teal)" stroke-width="2" d="M584,132 C680,122 780,125 860,132"/>
    </svg>

    <svg class="photo" width="860" height="612" viewBox="0 0 860 612" role="img" aria-label="Close-up portrait of a woman with glowing skin">
      <defs>
        <linearGradient id="skin" x1="0" y1="0" x2="1" y2="1">
          <stop offset="0" stop-color="#e9c4b2"/>
          <stop offset=".6" stop-color="#dba28e"/>
          <stop offset="1" stop-color="#c98874"/>
        </linearGradient>
      </defs>
      <path fill="url(#skin)" d="M588,140 C700,128 790,130 860,138 V405 C780,418 700,416 645,398 C612,370 598,300 588,140 Z"/>
    </svg>

    <svg class="photo" width="860" height="612" viewBox="0 0 860 612" role="img" aria-label="Portrait photo of the lead physician">
      <defs>
        <linearGradient id="doc" x1="0" y1="0" x2="0" y2="1">
          <stop offset="0" stop-color="#c9d3d6"/>
          <stop offset=".55" stop-color="#a57a62"/>
          <stop offset="1" stop-color="#27304a"/>
        </linearGradient>
      </defs>
      <circle cx="432" cy="284" r="96" fill="var(--teal)"/>
      <circle cx="432" cy="284" r="88" fill="url(#doc)" stroke="#dfe7e8" stroke-width="3"/>
    </svg>

    <section class="txt intro">
      <h2 class="section-title">CEDAR HOLLOW'S PREMIER MEDISPA</h2>
      <p class="section-copy">Solvane Vitality MediSpa is the premier medical spa in Cedar Hollow, TX. We utilize the best equipment available today for laser treatments, dermal fillers, facials, injections, chemical peels and wellness solutions.</p>
    </section>
    <section class="txt why">
      <h2 class="section-title">WHY CHOOSE OUR MEDISPA?</h2>
      <p class="section-copy">Under the supervision of Dr. Elena Hartwell, our medical staff provides state-of-the-art cosmetic treatments to both women and men.</p>
      <p class="section-copy">Our staff is trained to provide unique medical spa services to help our clients achieve a more youthful look and defy the aging process.</p>
    </section>
    <section class="txt members">
      <h2 class="section-title">EXCLUSIVE MEMBERSHIPS</h2>
      <p class="section-copy">Our exclusive membership packages are tailored for our clients and created to give them an exceptional experience at a discounted price.</p>
      <ul class="member-list">
        <li>SILVER Membership</li>
        <li>GOLD Membership</li>
        <li>PLATINUM Membership</li>
      </ul>
    </section>
    <section class="txt learn">
      <p class="learn-title">Learn More At</p>
      <p class="learn-url">www.SolvaneVitalityMedispa.com/memberships</p>
    </section>

    <section class="txt contact">
      <h3 class="contact-title">Location</h3>
      <p class="contact-line"><svg width="6" height="8" viewBox="0 0 6 8"><path d="M3,0 A3,3 0 0 1 6,3 C6,5 3,8 3,8 C3,8 0,5 0,3 A3,3 0 0 1 3,0Z" fill="#fff"/></svg>418 W. Cedar Hollow Pkwy Suite</p>
      <p class="contact-line contact-indent">210 Cedar Hollow TX 75500</p>
      <div class="contact-gap"></div>
      <h3 class="contact-title">Schedule a Consultation</h3>
      <p class="contact-line"><svg width="6" height="6" viewBox="0 0 6 6"><path d="M1,0 L2,2 L1.5,3 A4,4 0 0 0 3,4.5 L4,4 L6,5 L5,6 A5,5 0 0 1 0,1Z" fill="#fff"/></svg>(555) 014-2730</p>
      <p class="contact-line"><svg width="6" height="6" viewBox="0 0 6 6"><path d="M1,0 L2,2 L1.5,3 A4,4 0 0 0 3,4.5 L4,4 L6,5 L5,6 A5,5 0 0 1 0,1Z" fill="#fff"/></svg>(555) 016-4481</p>
      <p class="contact-line"><svg width="6" height="5" viewBox="0 0 6 5"><rect x=".3" y=".3" width="5.4" height="4.4" fill="none" stroke="#fff" stroke-width=".6"/><path d="M.3,.3 L3,2.6 L5.7,.3" fill="none" stroke="#fff" stroke-width=".6"/></svg>renewedglow@elenahartwellmd.com</p>
      <p class="contact-line"><svg width="6" height="6" viewBox="0 0 6 6"><circle cx="3" cy="3" r="2.6" fill="none" stroke="#fff" stroke-width=".6"/><path d="M.4,3 H5.6 M3,.4 C1.5,2 1.5,4 3,5.6 M3,.4 C4.5,2 4.5,4 3,5.6" fill="none" stroke="#fff" stroke-width=".5"/></svg>www.SolvaneVitalityMedispa.com</p>
    </section>
    <section class="txt doctor">
      <h3 class="doctor-name"><span>DR. ELENA HARTWELL,</span> MD FACS</h3>
      <p class="quote">"Rejuvenation and reconstruction of the face are my passion, whether it is to improve one's visual functions or to enhance one's appearance."</p>
      <p class="quote">"I personally perform all of my injections and CO2 laser treatments because safety and satisfaction are my top priorities."</p>
      <p class="quote">"I was called by God to become a physician at the age of seven years old. I am motivated by a desire to serve others by providing superb medical care. I constantly strive to do my best."</p>
    </section>

    <header class="txt brand">
      <p class="brand-name"><span class="brand-dot"></span>Solvane Vitality MediSpa</p>
      <p class="tagline">Refresh And Rejuvenate</p>
    </header>
    <h1 class="txt audience">FOR WOMEN AND MEN</h1>
    <ul class="txt services">
      <li>Laser Treatments</li><li>Facials</li>
      <li>Dermal Fillers</li><li>Chemical Peels</li>
      <li>Neurotoxins</li><li>Wellness Treatments</li>
    </ul>
    <div class="txt callout">
      <p class="callout-phone">(555) 014-2730</p>
      <p class="callout-url">www.SolvaneVitalityMedispa.com</p>
    </div>

  </article>
</main>
</body>
</html>
```